New hardcover book cover

I want a striking, eye-catching cover with title, subtitle and a picture.See for previous book covers: www.brightmaplepress.com

Target Market(s)

young, successful entrepreneurs that have built a business in a niche market that they discovered.

Font styles to use
Serif

Colors

Designer to choose colors to be used in the design.

Requirements
Must have
• A book cover that impresses and captures the imagination of those who look at it.
• MY MISTAKE, SORRY.
• Title: Founders Behind the Quiet Trade Boom
• Subtitle: 19 tales of triumph across
• uncovering unseen openings
• Author: Dennis Harwood
• Please use the photo attached, thanks.

```html
<!DOCTYPE html>
<html lang="en">
<head>
<meta charset="utf-8">
<title>Founders Behind the Quiet Trade Boom — Book Cover</title>
<link rel="stylesheet" href="https://fonts.googleapis.com/css2?family=PT+Serif:wght@400;700&display=swap">
<style>
  :root {
    --page-bg: #ffffff;
    --cover-purple-light: #472c80;
    --cover-purple: #3a2772;
    --cover-purple-dark: #2d2262;
    --beam: rgba(90, 100, 190, 0.26);
    --title-pink: #ee3d86;
    --subtitle-white: #ffffff;
    --glow-strong: rgba(236, 130, 165, 0.9);
    --glow-mid: rgba(214, 90, 150, 0.45);
    --glow-none: rgba(214, 90, 150, 0);
    --art-teal: #0b5a66;
  }
  * { margin: 0; padding: 0; box-sizing: border-box; }
  html, body {
    width: 1200px;
    height: 927px;
    overflow: hidden;
    background: var(--page-bg);
  }
  .stage {
    width: 1200px;
    height: 927px;
    display: flex;
    align-items: center;
    justify-content: center;
  }
  .book-cover {
    position: relative;
    width: 556px;
    height: 860px;
    overflow: hidden;
    background: linear-gradient(90deg, var(--cover-purple-light) 0%, var(--cover-purple) 55%, var(--cover-purple-dark) 100%);
    box-shadow: 0 10px 40px rgba(0, 0, 0, 0.25);
    font-family: "PT Serif", Georgia, serif;
    text-align: center;
  }
  .light-beam {
    position: absolute;
    inset: 0;
    width: 100%;
    height: 100%;
  }
  .cover-title {
    position: absolute;
    top: 50px;
    left: 0;
    right: 0;
    color: var(--title-pink);
    font-weight: 700;
    line-height: 53px;
  }
  .cover-title .title-large { font-size: 50px; }
  .cover-title .title-small { font-size: 38px; }
  .cover-subtitle {
    position: absolute;
    top: 246px;
    left: 0;
    right: 0;
    color: var(--subtitle-white);
    font-size: 31px;
    font-weight: 400;
    line-height: 40px;
  }
  .cover-art {
    position: absolute;
    left: 0;
    top: 330px;
    width: 556px;
    height: 440px;
    background:
      radial-gradient(ellipse 106px 148px at 188px 232px, var(--art-teal) 0 97%, transparent 100%),
      radial-gradient(circle 210px at 140px 96px, var(--glow-strong) 0%, var(--glow-mid) 40%, var(--glow-none) 100%);
  }
  .cover-author {
    position: absolute;
    top: 772px;
    left: 0;
    right: 0;
    color: var(--title-pink);
    font-size: 40px;
    font-weight: 700;
  }
</style>
</head>
<body>
  <main class="stage">
    <article class="book-cover">
      <svg class="light-beam" viewBox="0 0 556 860" preserveAspectRatio="none" aria-hidden="true">
        <polygon points="556,190 556,440 130,860 0,860 0,800" fill="var(--beam)"/>
      </svg>
      <div class="cover-art" role="img" aria-label="Illustration of an archery target with two pink darts in the bullseye, lit by a soft pink glow"></div>
      <h1 class="cover-title">
        <span class="title-large">Founders</span><br>
        <span class="title-small">Behind the</span> <span class="title-large">Quiet Trade</span><br>
        <span class="title-large">Boom</span>
      </h1>
      <p class="cover-subtitle">19 tales of triumph across<br>uncovering unseen openings</p>
      <p class="cover-author">Dennis Harwood</p>
    </article>
  </main>
</body>
</html>
```